Willowmere Counseling (Endure - Mend - Flourish) - Double Sided Business Card

I would like a 2-sided business card. Front: Matte Black or Navy with Logo & Tagline. Back: Name, Address, Phone Number, Email, & Website (maybe would like to include a small map pin-pointing location); Prefer front to be a gold/silver foil (iridescent); Back prefer white or light colored background with lettering that is easy to read and simple

Target Market(s)

Individuals & Couples (13 y.o. - ALL Adults); High end clientele

Industry/Entity Type

Licensed Professional Counselor (Mental Health)

Contact Information for Business Card

Name: Willowmere Counseling; Tagline: Endure - Mend - Flourish; Address: 3870 N. Garrick Ave., Suite 214, Fort Worth, TX 76132; Phone: (214) 555-0187; Website: www.WillowmereCounseling.example

Font styles to use
Serif

Requirements
Must have
• Logo on Front (Large) prefer gold/silver foil on a matte dark color (i.e. black, navy, etc.); Back of Card: All other relevant information

```html
<!DOCTYPE html>
<html lang="en">
<head>
<meta charset="utf-8">
<title>Willowmere Counseling – Business Card</title>
<link rel="stylesheet" href="https://fonts.googleapis.com/css2?family=Cinzel:wght@400;600&display=swap">
<style>
  :root {
    --backdrop: #5e5f62;
    --card-dark: #1f1f1f;
    --card-light: #f4f4f2;
    --gold: #d9b23a;
    --gold-edge: #cfa92c;
    --slate: #8a8a8c;
    --ink: #6f6f71;
  }
  * { margin: 0; padding: 0; box-sizing: border-box; }
  html, body { width: 1200px; height: 1050px; overflow: hidden; }
  body {
    background: var(--backdrop);
    font-family: "Cinzel", serif;
    display: flex;
    flex-direction: column;
    align-items: center;
    justify-content: center;
    gap: 40px;
  }
  .card {
    width: 820px;
    height: 469px;
    display: flex;
    flex-direction: column;
    align-items: center;
    justify-content: center;
    border-bottom: 6px solid var(--gold-edge);
    box-shadow: 0 12px 28px rgba(0,0,0,0.35);
  }
  .card--front { background: var(--card-dark); }
  .card--back { background: var(--card-light); }

  .brand { display: flex; flex-direction: column; align-items: center; }
  .brand__mark {
    width: 70px; height: 70px; border-radius: 50%;
    background: var(--gold);
    margin-bottom: 18px;
  }
  .card--back .brand__mark { width: 56px; height: 56px; margin-bottom: 14px; }
  .brand__name {
    color: var(--gold);
    font-weight: 600;
    font-size: 46px;
    letter-spacing: 3px;
    text-align: center;
    line-height: 1.15;
  }
  .card--back .brand__name { font-size: 36px; }
  .brand__rule {
    width: 420px; height: 2px;
    background: var(--gold);
    margin: 14px 0 12px;
  }
  .card--back .brand__rule { background: var(--slate); width: 340px; margin: 10px 0; }
  .brand__tagline {
    color: var(--gold);
    font-size: 17px;
    letter-spacing: 3px;
  }
  .card--back .brand__tagline { font-size: 14px; }

  .contact {
    margin-top: 30px;
    text-align: center;
    color: var(--ink);
    font-size: 17px;
    letter-spacing: 1.5px;
    line-height: 1.8;
  }
  .contact__phone { font-size: 21px; letter-spacing: 2px; }
</style>
</head>
<body>
  <section class="card card--front" aria-label="Card front">
    <div class="brand">
      <div class="brand__mark" aria-hidden="true"></div>
      <h1 class="brand__name">Willowmere Counseling</h1>
      <div class="brand__rule"></div>
      <p class="brand__tagline">Endure - Mend - Flourish</p>
    </div>
  </section>

  <section class="card card--back" aria-label="Card back">
    <div class="brand">
      <div class="brand__mark" aria-hidden="true"></div>
      <h2 class="brand__name">Willowmere Counseling</h2>
      <div class="brand__rule"></div>
      <p class="brand__tagline">Endure - Mend - Flourish</p>
    </div>
    <address class="contact" style="font-style: normal;">
      <p class="contact__phone">(214) 555-0187</p>
      <p class="contact__web">www.WillowmereCounseling.example</p>
      <p class="contact__address">3870 N. Garrick Ave., Suite 214, Fort Worth, TX 76132</p>
    </address>
  </section>
</body>
</html>
```